Tera Vox

Graphic design for web pages depicting an environmental solution to human waste streams of plastic, tyres and bio mass, converting waste to energy. Technology used is a pyrolysis plant deconstructing 20tonnes per day of waste. Also touch up of logo

```html
<!DOCTYPE html>
<html lang="en">
<head>
<meta charset="utf-8">
<title>Tera Vox – Waste to Energy</title>
<link href="https://fonts.googleapis.com/css2?family=Lato:wght@400;700;900&display=swap" rel="stylesheet">
<style>
  :root {
    --sky: #dff4fb;
    --sky-deep: #c6e8f1;
    --city: #b9dfe9;
    --grass: #86c94a;
    --grass-dark: #72b83c;
    --navy: #1d4f8c;
    --teal: #138b8e;
    --body-text: #333b40;
    --button-start: #1a7a8a;
    --button-end: #1b4f86;
    --white: #ffffff;
  }
  * { margin: 0; padding: 0; box-sizing: border-box; }
  html, body { width: 1200px; height: 375px; overflow: hidden; }
  body { font-family: "Lato", Arial, sans-serif; background: var(--sky); }

  .hero { position: relative; width: 1200px; height: 375px; overflow: hidden; background: var(--sky); }

  .hero-scene {
    position: absolute; left: 0; right: 0; top: 130px; bottom: 0;
    background: linear-gradient(180deg,
      var(--sky) 0%,
      var(--sky-deep) 35%,
      var(--city) 60%,
      #a9d98a 78%,
      var(--grass) 86%,
      var(--grass-dark) 93%,
      var(--sky) 96%,
      var(--sky) 100%);
  }

  .hero-content {
    position: relative; z-index: 1;
    display: flex; flex-direction: column; align-items: center;
    text-align: center;
  }

  .brand { margin-top: 19px; display: flex; flex-direction: column; align-items: center; }
  .brand-square { width: 30px; height: 30px; background: var(--teal); }
  .brand-name { margin-top: 6px; font-size: 8px; font-weight: 400; color: var(--navy); letter-spacing: 0.2px; }

  .hero-title {
    margin-top: 18px;
    font-size: 30px; font-weight: 900; color: var(--navy);
    letter-spacing: 0.2px; line-height: 1;
  }
  .hero-text {
    margin-top: 11px; width: 440px;
    font-size: 12.5px; line-height: 18px; color: var(--body-text);
  }
  .hero-button {
    margin-top: 20px;
    display: inline-flex; align-items: center; justify-content: center;
    width: 134px; height: 37px; border-radius: 19px;
    background: linear-gradient(180deg, var(--button-start), var(--button-end));
    color: var(--white); font-size: 12.5px; font-weight: 700;
    text-decoration: none; letter-spacing: 0.2px;
  }
</style>
</head>
<body>
  <section class="hero">
    <div class="hero-scene" role="img" aria-label="Illustration of a green city skyline with wind turbines, trees, recycling bins, a yellow recycling truck and a recycling plant"></div>
    <div class="hero-content">
      <div class="brand">
        <span class="brand-square"></span>
        <span class="brand-name">Tera Vox</span>
      </div>
      <h1 class="hero-title">ETIAM NON DIAM IN ODIO SUSCIPIT HENDRERIT</h1>
      <p class="hero-text">Donec sit amet risus nibh. Proin suscipit, tortor vel pretium convallis, odio lorem varius tortor, ut blandit risus sapien dapibus lacus.</p>
      <a class="hero-button" href="#">READ MORE</a>
    </div>
  </section>
</body>
</html>
```